Investment Fund Investor newsletter

I deleted the tear sheet example which was provided for design purposes only and not for content. Please see the simple outline for the newsletter and the related sections.

Please be clear this project is for a newsletter template. This means a template that can be updated on a monthly or quarterly basis with new content for our audience. Sections should include: Operations Update, Financial Update, Energy Investor News.

We need a template for a newsletter that can be sent out in Word format and also able to send out via Mailchimp. Audience are current investors in our oil and gas fund. These investors are high net worth individuals and private equity firms so the branding needs to be high end, sophisticated and corporate. Please see website and attached tear sheet for the type of branding that we want to match. Website is www.quarrybell-power.com
Please see website and tear sheet for the color scheme that we want.

Target Market(s)

Our current fund investors that include high net worth investors and CEOs of private equity companies

Industry/Entity Type

oil and gas... investment

Font styles to use
Serif

Requirements
Must have
• Word file and can send via Mailchimp too

```html
<!DOCTYPE html>
<html lang="en">
<head>
<meta charset="utf-8">
<title>Quarrybell Power Partners II – LP Update Q4 2022</title>
<link rel="stylesheet" href="https://fonts.googleapis.com/css2?family=Fira+Sans+Extra+Condensed:wght@600&family=PT+Sans:wght@700&family=Source+Serif+4:wght@400;600&display=swap">
<style>
  :root {
    --brand-blue: #00a3e0;
    --charcoal: #333436;
    --column-grey: #e6e6e7;
    --page-white: #ffffff;
    --body-text: #333333;
    --link-blue: #1a1ad6;
    --backdrop: #6a6a6a;
    --photo-sky: #c98aa6;
    --photo-dusk: #5e5f86;
    --photo-ground: #2f4a52;
  }
  * { margin: 0; padding: 0; box-sizing: border-box; }
  html, body {
    width: 1200px; height: 900px; overflow: hidden;
    background: var(--backdrop);
  }
  .newsletter {
    position: absolute; left: 252px; top: 0;
    width: 695px; height: 900px;
    background: var(--page-white);
    overflow: hidden;
  }
  .page-shapes {
    position: absolute; inset: 0; width: 100%; height: 100%;
  }
  .brand-name {
    position: absolute; left: 32px; top: 112px; width: 162px;
    font-family: "Source Serif 4", serif; font-weight: 600;
    color: var(--charcoal); text-align: center; line-height: 1;
  }
  .brand-name .brand-primary { display: block; font-size: 18px; letter-spacing: 3px; }
  .brand-name .brand-secondary { display: block; font-size: 8px; letter-spacing: 4.6px; margin-top: 5px; }
  .issue-title {
    position: absolute; left: 32px; top: 289px;
    font-family: "Fira Sans Extra Condensed", sans-serif; font-weight: 600;
    font-size: 27px; line-height: 31px; color: var(--charcoal);
  }
  .section-heading {
    font-family: "PT Sans", sans-serif; font-weight: 700;
    font-size: 17.5px; color: var(--brand-blue); margin-bottom: 9px;
  }
  .section-body p {
    font-family: "Source Serif 4", serif; font-size: 11.9px; line-height: 14.45px;
    color: var(--body-text); margin-bottom: 14.4px;
  }
  .operations-update { position: absolute; left: 32px; top: 378px; width: 218px; }
  .financial-update { position: absolute; left: 289px; top: 378px; width: 375px; }
  .investor-news { position: absolute; left: 323px; top: 749px; width: 350px; }
  .investor-news .section-heading { color: var(--page-white); margin-bottom: 6px; }
  .news-links { list-style: none; }
  .news-links li { line-height: 21.7px; }
  .news-links a {
    font-family: "Source Serif 4", serif; font-size: 11.6px;
    color: var(--link-blue); text-decoration: underline;
  }
  .site-address {
    position: absolute; left: 32px; top: 875px;
    font-family: "PT Sans", sans-serif; font-weight: 700; font-size: 11px;
    color: var(--page-white);
  }
</style>
</head>
<body>
<article class="newsletter">
  <svg class="page-shapes" viewBox="0 0 1026 1328" preserveAspectRatio="none" aria-hidden="false">
    <defs>
      <linearGradient id="refinery-dusk" x1="0" y1="0" x2="0" y2="1">
        <stop offset="0" stop-color="var(--photo-sky)"/>
        <stop offset="0.3" stop-color="var(--photo-dusk)"/>
        <stop offset="1" stop-color="var(--photo-ground)"/>
      </linearGradient>
    </defs>
    <rect class="column-panel" x="0" y="527" width="393" height="753" fill="var(--column-grey)"/>
    <polygon class="title-band" points="0,304 839,304 712,527 0,527" fill="var(--brand-blue)"/>
    <polygon class="accent-block" points="827,328 1026,328 1026,468 747,468" fill="var(--charcoal)"/>
    <g role="img" aria-label="Photograph of an oil refinery with storage tanks lit up at dusk under a sunset sky">
      <polygon class="hero-photo" points="437,0 1026,0 1026,328 827,328 782,404 200,404" fill="url(#refinery-dusk)"/>
    </g>
    <polygon class="footer-band" points="0,1279 352,1279 324,1328 0,1328" fill="var(--charcoal)"/>
    <polygon class="news-panel" points="465,1081 1026,1081 1026,1328 322,1328" fill="var(--brand-blue)"/>
  </svg>

  <div class="brand-name">
    <span class="brand-primary">QUARRYBELL</span>
    <span class="brand-secondary">POWER PARTNERS</span>
  </div>

  <h1 class="issue-title">Quarrybell Power Partners II: LP Update<br>Q4 2022 Update</h1>

  <section class="operations-update">
    <h2 class="section-heading">Operations Update</h2>
    <div class="section-body">
      <p>Nemo enim ipsam voluptatem, quia voluptas sit, aspernatur aut odit aut fugit, sed quia consequuntur magni dolores eos, qui ratione voluptatem sequi nesciunt, neque porro quisquam est, qui dolorem ipsum, quia dolor sit amet consectetur adipisci velit, sed quia non numquam eius modi tempora incidunt, ut labore et dolore magnam aliquam quaerat voluptatem.</p>
      <p>Ut enim ad minima veniam, quis nostrum exercitationem ullam corporis suscipit laboriosam, nisi ut aliquid ex ea commodi consciunt, neque porro quisquam est, qui dolorem ipsum, quia dolor sit amet consectetur adipisci velit, sed quia non numquaequatur? qui dolorem ipsum, quia dolor sit amet consectetur adipisci velit, sed quia non numquam eius modi tempora incidunt, ut labore et dolore magnam aliquam quaerat voluptatem.</p>
      <p>Quis autem vel eum iure reprehenderit, qui in ea voluptate velit esse, quam nihil molestiae consequatur, vel illum, qui dolorem eum fugiat, quo voluptas nulla pariatur?</p>
    </div>
  </section>

  <section class="financial-update">
    <h2 class="section-heading">Financial Update</h2>
    <div class="section-body">
      <p>Nemo enim ipsam voluptatem, quia voluptas sit, aspernatur aut odit aut fugit, sed quia consequuntur magni dolores eos, qui ratione voluptatem snesciunt, neque porro quisquam est, qui dolorem ipsum, quia dolor sit amet consectetur adipisci velit, sed quia non numqequi nesciunt, neque porro quisquam est, qui dolorem ipsum, quia dolor sit amet consectetur adipisci velit, sed quia non numquam eius modi tempora incidunt, ut labore et dolore magnam.</p>
      <p>Ut enim ad minima veniam, quis nostrum exercitationem ullam corporis nesciunt, neque porro quisquam est, qui dolorem ipsum, quia dolor sit amenesciunt, neque porro quisquam est, qui dolorem ipsum, quia dolor sit amet consectetur adipisci velit, sed quia non numqt consectetur adipisci velit, sed quia non numqsuscipit laboriosam, nisi ut aliquid ex ea commodi consequatur?</p>
      <p>Quis autem vel eum iure reprehenderit, qui in ea voluptate velit esse, quam ninesciunt, neque porro quisquam est, qui dolorem ipsum, quia dolor sit amet consectetur adipisci velit, sed quia non numqhnesciunt, neque porro quisquam est, qui dolorem ipsum, quia dolor sit amet consectetur adipisci velit, sed quia non numqil molestiae consequatur, vel illum, qui dolorem eum fugiat, quo voluptas nulla pariatur?</p>
    </div>
  </section>

  <section class="investor-news">
    <h2 class="section-heading">Energy Investor News</h2>
    <ul class="news-links">
      <li><a href="#">Will Allied Producers Group Cut Production on Labor Day? (crudewire.net)</a></li>
      <li><a href="#">Harlan Whitcomb Keeps Betting Big on Oil (Ridgeway Markets)</a></li>
      <li><a href="#">'What is Behind Wall Streets $100 oil Forecast?&nbsp; (Daily Ledger)</a></li>
    </ul>
  </section>

  <footer class="site-address">www.quarrybell-power.com</footer>
</article>
</body>
</html>
```